Gelato Business Card

create a new business card using existing logo

Target Market(s)

B2B

Contact Information for Business Card

typical contact info: logo, address, email, phone, rep name

Colors
0355a3
33a6d7

Requirements
Must have
• a feel of high quality, luxury, happiness
• use cool, comforting color and texture of business card.
Nice to have
• "A Little Perfection Goes A Long Way!" TM
• or, "more quality, more flavor"
• or, "Flavor Matters"

```html
<!DOCTYPE html>
<html lang="en">
<head>
<meta charset="utf-8">
<title>Brivella Gelato — Business Card</title>
<link rel="stylesheet" href="https://fonts.googleapis.com/css2?family=Montserrat:wght@500;600&family=Cormorant+Garamond:ital,wght@1,500&display=swap">
<style>
  :root {
    --backdrop: #262628;
    --card: #1b1b1d;
    --card-edge: #2a2a2d;
    --texture: #2a2a2e;
    --violet: #6a64cc;
    --violet-soft: #8580d8;
    --ink: #f4f4f6;
  }
  * { margin: 0; padding: 0; box-sizing: border-box; }
  html, body { width: 1200px; height: 900px; overflow: hidden; }
  body {
    background: var(--backdrop);
    font-family: "Montserrat", sans-serif;
    display: flex;
    flex-direction: column;
    align-items: center;
    justify-content: center;
    gap: 40px;
  }
  .card {
    width: 700px;
    height: 400px;
    background: var(--card);
    border: 1px solid var(--card-edge);
    border-radius: 28px;
    position: relative;
    overflow: hidden;
    box-shadow: 0 10px 30px rgba(0,0,0,.45);
  }
  .card-texture {
    position: absolute;
    inset: 0;
    background:
      radial-gradient(ellipse at 20% 25%, var(--texture) 0%, transparent 45%),
      radial-gradient(ellipse at 80% 30%, var(--texture) 0%, transparent 45%),
      radial-gradient(ellipse at 30% 80%, var(--texture) 0%, transparent 45%),
      radial-gradient(ellipse at 78% 82%, var(--texture) 0%, transparent 45%);
    opacity: 0.9;
  }
  .card-watermark {
    position: absolute;
    left: 330px;
    top: 40px;
    width: 220px;
    height: 320px;
    border-radius: 50%;
    background: radial-gradient(ellipse at center, #242427 0%, #202023 55%, transparent 72%);
  }
  .brand {
    position: relative;
    display: flex;
    align-items: center;
    gap: 14px;
    color: var(--violet-soft);
    font-weight: 600;
    letter-spacing: 0.04em;
    white-space: nowrap;
  }
  .brand-dot {
    border-radius: 50%;
    background: var(--violet);
    flex: none;
  }
  .card-front { display: flex; align-items: center; justify-content: center; }
  .card-front .brand { font-size: 40px; }
  .card-front .brand-dot { width: 34px; height: 34px; }
  .card-back .brand {
    position: absolute;
    left: 60px;
    top: 150px;
    font-size: 27px;
  }
  .card-back .brand-dot { width: 24px; height: 24px; }
  .contact {
    position: absolute;
    left: 400px;
    top: 122px;
    color: var(--ink);
  }
  .contact-name { font-size: 27px; font-weight: 600; letter-spacing: 0.02em; }
  .contact-title {
    font-family: "Cormorant Garamond", serif;
    font-style: italic;
    font-weight: 500;
    font-size: 19px;
    color: var(--violet-soft);
    margin: 0 0 20px 2px;
  }
  .contact-list { list-style: none; }
  .contact-list li {
    display: flex;
    align-items: center;
    gap: 12px;
    font-size: 18px;
    font-weight: 500;
    margin-bottom: 10px;
  }
  .contact-list svg { width: 18px; height: 18px; fill: var(--violet); flex: none; }
</style>
</head>
<body>
  <section class="card card-front">
    <div class="card-texture" role="img" aria-label="Faint repeated brand-symbol pattern across the card"></div>
    <div class="brand"><span class="brand-dot"></span>Brivella Gelato</div>
  </section>

  <section class="card card-back">
    <div class="card-watermark" role="img" aria-label="Large faint brand symbol in the background"></div>
    <div class="brand"><span class="brand-dot"></span>Brivella Gelato</div>
    <div class="contact">
      <p class="contact-name">Your Name</p>
      <p class="contact-title">Job Title</p>
      <ul class="contact-list">
        <li>
          <svg viewBox="0 0 24 24" aria-hidden="true"><path d="M6.6 10.8a15.1 15.1 0 0 0 6.6 6.6l2.2-2.2c.3-.3.7-.4 1-.2 1.1.4 2.3.6 3.6.6.6 0 1 .4 1 1V20c0 .6-.4 1-1 1A17 17 0 0 1 3 4c0-.6.4-1 1-1h3.5c.6 0 1 .4 1 1 0 1.3.2 2.5.6 3.6.1.3 0 .7-.2 1z"/></svg>
          000 000 0000
        </li>
        <li>
          <svg viewBox="0 0 24 24" aria-hidden="true"><path d="M2 5h20v14H2zm2 2v.5l8 5 8-5V7zm0 2.9V17h16V9.9l-8 5z"/></svg>
          youremail@xyz.com
        </li>
        <li>
          <svg viewBox="0 0 24 24" aria-hidden="true"><path d="M12 2a7 7 0 0 0-7 7c0 5.2 7 13 7 13s7-7.8 7-13a7 7 0 0 0-7-7zm0 9.5A2.5 2.5 0 1 1 12 6.5a2.5 2.5 0 0 1 0 5z"/></svg>
          Your Address here
        </li>
      </ul>
    </div>
  </section>
</body>
</html>
```